CBD online business for pets and pet parents needs a new website

We need a website for my new online business. I have left a job of 25 years to do my passion. Helping Pets Live healthy and happy lives. I would like to provide my story so that our customer will know why I have started this business-To help!We will be providing all natural CBD (Hemp) products, specialty items, memorials as well as some products for pet parents. We would like our landing page to have our mission, be informative and easy to navigate and maybe feature our treats and oils for pets. We will need a page for pet products, a page for pet memorials, a page for pet lover products and a page for pet parent products.

Target Market(s)

millennials, boomers, pet lovers

Coding

Coded - Design and coding required

Number of Pages Required

5+ page

Colors
33b8a4

Requirements
Nice to have
• diagram of hemp oil extract benefits for dogs and people

```html
<!DOCTYPE html>
<html lang="en">
<head>
<meta charset="utf-8">
<title>Kindtail Co – Login</title>
<link href="https://fonts.googleapis.com/css2?family=Montserrat:wght@400;500;600;700&family=Kaushan+Script&display=swap" rel="stylesheet">
<style>
:root{
  --teal:#00a5a8;
  --teal-soft:#e7f6f6;
  --ink:#2b2b2b;
  --text:#3a3a3a;
  --muted:#8a8a8a;
  --line:#cfcfcf;
  --panel:#f3f3f3;
  --dark:#2e2f33;
  --white:#fff;
}
*{box-sizing:border-box;margin:0;padding:0}
html,body{width:1038px;height:1200px;overflow:hidden}
body{position:relative;background:var(--white);font-family:'Montserrat',sans-serif;color:var(--text)}
.abs{position:absolute}
.topbar{left:0;top:0;width:1038px;height:3px;background:var(--teal)}
.header{left:0;top:3px;width:1038px;height:106px;background:var(--white)}
.lang{left:110px;top:18px;width:99px;height:30px;border:1px solid #555;border-radius:15px;font-size:11px;display:flex;align-items:center;padding-left:15px;gap:7px;color:var(--ink)}
.lang .flag{width:12px;height:12px;border-radius:50%;background:#c9d2e6}
.social-top{left:230px;top:26px;display:flex;gap:14px}
.social-top span{width:15px;height:15px;border-radius:50%;background:#8d8d8d;display:block}
.search{left:684px;top:18px;width:160px;height:30px;border:1px solid #555;border-radius:15px;overflow:hidden;font-size:10px;color:#666;padding:9px 0 0 17px}
.search .btn{position:absolute;right:2px;top:2px;width:32px;height:24px;background:var(--teal);border-radius:0 13px 13px 0}
.cart{left:864px;top:26px;font-size:11px;color:var(--ink);display:flex;gap:8px;align-items:center}
.rule{height:1px;background:var(--line);top:63px}
.nav{top:79px;font-size:12.5px;color:var(--ink)}
.nav.active{color:var(--teal)}
.nav-underline{left:861px;top:106px;width:67px;height:3px;background:var(--teal)}
.brand-badge{left:429px;top:60px;width:180px;height:72px;background:var(--white);border-radius:0 0 30px 30px}
.brand-name{left:429px;top:96px;width:180px;text-align:center;font-weight:700;font-size:20px;color:var(--teal)}
.brand-dot{left:503px;top:30px;width:32px;height:32px;border-radius:50%;background:var(--teal)}
.hero-text h1{left:140px;top:150px;font-size:40px;font-weight:700;letter-spacing:-1.5px;color:var(--teal)}
.hero-text p{left:140px;top:204px;font-family:'Kaushan Script',cursive;font-size:30px;color:var(--ink)}
.crumbs{left:139px;top:368px;font-size:11px;color:#555;display:flex;gap:16px}
.crumbs .current{color:var(--teal);font-weight:500}
.login-mark{left:504px;top:448px;width:30px;height:30px;border-radius:50%;background:var(--teal)}
.login-title{left:419px;top:492px;width:200px;text-align:center;font-size:30px;font-weight:700;letter-spacing:-1.5px;color:var(--ink)}
.login-underline{left:498px;top:536px;width:42px;height:2px;background:var(--teal)}
.login-box{left:350px;top:557px;width:338px;height:225px;background:var(--panel);border:1px solid #e2e2e2;border-bottom:3px solid var(--teal)}
.field{left:383px;width:272px;height:34px;background:var(--white);border:1px solid #dedede;border-radius:17px;font-size:9.5px;letter-spacing:1px;color:#666;padding:11px 0 0 18px}
.login-btn{left:383px;top:683px;width:272px;height:39px;background:var(--teal);border-radius:20px;color:var(--white);font-size:14px;font-weight:500;text-align:center;line-height:39px}
.login-links{left:382px;top:734px;width:273px;font-size:9.5px;display:flex;justify-content:space-between}
.login-links a{color:var(--teal);text-decoration:none}
.login-links span{color:var(--ink)}
.footer{left:0;top:845px;width:1038px;height:307px;background:var(--dark)}
.foot-title{top:913px;font-size:13px;font-weight:700;color:var(--white);letter-spacing:-.5px}
.foot-title em{font-family:'Kaushan Script',cursive;font-style:normal;font-weight:400;color:var(--teal);font-size:14px}
.foot-bar{top:940px;width:23px;height:2px;background:var(--teal)}
.quick{left:141px;top:952px;font-size:11px;color:var(--white);line-height:20.8px;list-style:none}
.contact-brand{left:318px;top:957px;font-size:12px;font-weight:700;color:var(--teal)}
.contact-line{left:319px;font-size:10px;color:var(--white);line-height:17px}
.ico{left:293px;width:13px;height:13px;fill:var(--white)}
.news-text{left:531px;top:953px;font-size:10.5px;letter-spacing:1px;color:var(--white);line-height:14.5px}
.news-field{left:528px;width:181px;height:32px;border:1px solid #8a8a8a;border-radius:16px;font-size:9px;letter-spacing:1px;color:#999;padding:10px 0 0 13px}
.news-btn{left:528px;top:1068px;width:96px;height:38px;background:var(--teal);border-radius:19px;color:var(--white);font-size:13px;font-weight:600;text-align:center;line-height:38px}
.foot-brand-dot{left:815px;top:915px;width:34px;height:34px;border-radius:50%;background:#8d8d8d}
.foot-brand{left:760px;top:992px;width:144px;text-align:center;font-size:18px;font-weight:700;color:#a7a7a7}
.follow-circles{left:776px;top:1077px;display:flex;gap:7px}
.follow-circles span{width:25px;height:25px;border-radius:50%;border:1px solid #8a8a8a;display:block}
.follow-circles span.on{background:var(--teal);border-color:var(--teal)}
.bottom-band{left:0;top:1152px;width:1038px;height:48px;background:var(--teal);color:var(--white);font-size:10.5px;letter-spacing:1px}
.bottom-band .copy{position:absolute;left:140px;top:21px}
.bottom-band .legal{position:absolute;left:663px;top:24px}
</style>
</head>
<body>
<div class="abs topbar"></div>
<header class="abs header"></header>

<div class="abs lang"><span class="flag"></span>English ▾</div>
<div class="abs social-top"><span></span><span></span><span></span><span></span><span></span></div>
<div class="abs search">Search...<span class="btn"></span></div>
<div class="abs cart">
  <svg width="13" height="12" viewBox="0 0 13 12"><path d="M0 1h2.5l2 7h6l1.5-5H4" fill="none" stroke="#2b2b2b" stroke-width="1.5"/><circle cx="5" cy="10.5" r="1.2" fill="#2b2b2b"/><circle cx="10" cy="10.5" r="1.2" fill="#2b2b2b"/></svg>
  Cart (0)
</div>
<div class="abs rule" style="left:110px;width:296px"></div>
<div class="abs rule" style="left:632px;width:296px"></div>
<nav>
  <span class="abs nav" style="left:112px">Home</span>
  <span class="abs nav" style="left:208px">About Us</span>
  <span class="abs nav" style="left:313px">Pet Products ▾</span>
  <span class="abs nav" style="left:633px">Our Mission</span>
  <span class="abs nav" style="left:732px">Benefits</span>
  <span class="abs nav" style="left:807px">Blog</span>
  <span class="abs nav active" style="left:861px">Contact Us</span>
</nav>
<div class="abs nav-underline"></div>

<svg class="abs" style="left:0;top:109px" width="1038" height="280" viewBox="0 0 1038 280">
  <rect width="1038" height="280" fill="#e7f6f6"/>
  <defs>
    <linearGradient id="heroTone" x1="0" x2="1" y1="0" y2="1">
      <stop offset="0" stop-color="#cfd6d4"/>
      <stop offset=".5" stop-color="#b7a98a"/>
      <stop offset=".8" stop-color="#8d7a62"/>
      <stop offset="1" stop-color="#6f6a5e"/>
    </linearGradient>
  </defs>
  <path role="img" aria-label="Photo of a smiling woman hugging a happy yellow labrador outdoors" d="M0 0H1038V100C860 220 660 246 519 246C360 246 150 220 0 100Z" fill="url(#heroTone)"/>
  <path d="M0 96C150 216 360 244 519 244C660 244 860 218 1038 96" fill="none" stroke="#00a5a8" stroke-width="9"/>
</svg>

<div class="abs brand-badge"></div>
<div class="abs brand-dot"></div>
<div class="abs brand-name">Kindtail Co</div>

<div class="hero-text">
  <h1 class="abs">Helping Pets</h1>
  <p class="abs">Live healthy and happy lives</p>
</div>

<div class="abs crumbs"><span>Home</span><span>›</span><span class="current">Login</span></div>

<div class="abs login-mark"></div>
<h2 class="abs login-title">Login</h2>
<div class="abs login-underline"></div>

<div class="abs login-box"></div>
<div class="abs field" style="top:589px">Email*</div>
<div class="abs field" style="top:636px">Password*</div>
<div class="abs login-btn">Login</div>
<div class="abs login-links"><a href="#">Forgot Password?</a><span>New Customer? <a href="#">Register</a></span></div>

<footer class="abs footer"></footer>

<h3 class="abs foot-title" style="left:140px">Quick <em>Links</em></h3>
<div class="abs foot-bar" style="left:140px"></div>
<ul class="abs quick">
  <li>› Home</li><li>› About Us</li><li>› Pet Products ▾</li><li>› Our Mission</li><li>› Benefits</li><li>› Blog</li><li>› Contact Us</li>
</ul>

<h3 class="abs foot-title" style="left:293px">Contact <em>Details</em></h3>
<div class="abs foot-bar" style="left:293px"></div>
<svg class="abs ico" style="top:957px;height:18px" viewBox="0 0 12 18"><path d="M6 0a6 6 0 0 0-6 6c0 4.5 6 12 6 12s6-7.5 6-12a6 6 0 0 0-6-6zm0 8.5A2.5 2.5 0 1 1 6 3.5a2.5 2.5 0 0 1 0 5z"/></svg>
<div class="abs contact-brand">Kindtail Co</div>
<div class="abs contact-line" style="top:975px">Lorem ipsum dolor sit amet,<br>consectetur adipiscing elit</div>
<svg class="abs ico" style="top:1016px" viewBox="0 0 14 14"><path d="M3 0l2.5 3.5-1.5 1.5a8 8 0 0 0 5 5l1.5-1.5L14 11l-2 3C5 13 1 9 0 2z"/></svg>
<div class="abs contact-line" style="top:1016px;font-size:12px;letter-spacing:1px">(123) 456 7890</div>
<svg class="abs ico" style="top:1046px;width:14px;height:11px" viewBox="0 0 14 11"><path d="M0 0h14v1.5L7 6 0 1.5zM0 3l7 4.5L14 3v8H0z"/></svg>
<div class="abs contact-line" style="top:1043px;font-size:11px">hello@kindtailco.com</div>

<h3 class="abs foot-title" style="left:530px">Newsletter <em>Subscription</em></h3>
<div class="abs foot-bar" style="left:530px"></div>
<p class="abs news-text">Subscribe to our newsletter<br>for latest updates.</p>
<div class="abs news-field" style="top:991px">Your Name*</div>
<div class="abs news-field" style="top:1030px">Your Email Address*</div>
<div class="abs news-btn">Sign Up</div>

<div class="abs foot-brand-dot"></div>
<div class="abs foot-brand">Kindtail Co</div>
<h3 class="abs foot-title" style="left:774px;top:1033px">Follow <em>Us On:</em></h3>
<div class="abs foot-bar" style="left:775px;top:1059px"></div>
<div class="abs follow-circles"><span class="on"></span><span></span><span></span><span></span></div>

<div class="abs bottom-band">
  <span class="copy">© 2019. Kindtail Co. All Right Reserved.</span>
  <span class="legal">Privacy Policy &nbsp;&nbsp;/&nbsp;&nbsp; Terms &amp; Conditions</span>
</div>
</body>
</html>
```